International Petrochemical business needs a web design for Tessaro Desk system

We need a web design for a "Tessaro Desk" system for an international petrochemical company. The web site is used internally within the company. It is hosted by an internal department which provides government permit request service for other departments.

We would like to see designs of two pages using color light blue. (home page, internal page as attached).
Home Page:
1. Header has a background image and small animation. Header on home page can be taller than the header of the internal page.
2. Layout as attached.

Internal Page:
1. Header can use the same background image as the home page and can be shorter to utilize the page for content.
2. The blue icon behind every captions represent an icon. When user move mouse over this icon, it displays the caption in Thai language as a tooltip. This icon needs to be redesign.

The final design should communicate the followings:
- Excellent service provided system in terms of time and accurary
- Rapid growth of business via building petrochemical refinery plant

For Internal Page, the blue circle behind every captions represent an icon. When mouse over this icon, a tool tip showing the caption in Thai language is shown. Please also design this icon..

There are more feedbacks from customer as followed:

1. Banner should consists of 
    1.1 "Approved" stamp on paper
    1.2 An image of Garuda. It is used on every government documents in Thailand
    1.3 Image of petrochemical plant
2. Each menu item (Home, Permit, Search, etc) should have different colors. Drop down menu will use the same color as its parent menu item.
3. Overall tone of the web page should be light blue with background of the body the web page in white
4. "New Request" button should use green color with icon on it
5. Table header of each box in the body of the page should use dark blue background with text in white

Please kindly submit your revisions.
Thank you.

Reason: We get some late feedbacks from customers which was just updated to all designers.

• 1. Design for 1024x768 screen resolution
2. Use light blue theme
3. Background of header where the company logo is must have white background

```html
<!DOCTYPE html>
<html lang="en">
<head>
<meta charset="utf-8">
<title>Tessaro Desk – Home</title>
<link rel="stylesheet" href="https://fonts.googleapis.com/css2?family=Bree+Serif&family=Open+Sans:ital,wght@0,400;0,600;0,700;1,400&display=swap">
<style>
:root{
  --sky:#00a8e6;
  --sky-deep:#0c6f9e;
  --ink:#2d2d2d;
  --head:#333333;
  --body-grey:#e1e1e1;
  --white:#ffffff;
  --rule:#d9d9d9;
  --link:#1b5fb5;
  --text:#444444;
  --green-top:#a6e05a;
  --green-bot:#74c12b;
  --pager-dark:#4a5a78;
}
*{box-sizing:border-box;margin:0;padding:0}
html,body{width:1152px;height:1200px;overflow:hidden}
body{position:relative;background:var(--body-grey);font-family:"Open Sans",Arial,sans-serif;color:var(--text)}
.sky-band{position:absolute;left:0;top:0;width:1152px;height:329px;background:linear-gradient(180deg,#12b2ec 0%,var(--sky) 60%,#08a2df 100%)}
.topbar{position:absolute;left:0;top:0;width:1152px;height:43px;background:linear-gradient(180deg,#13a9e4,#0b8fcc);box-shadow:0 3px 6px rgba(0,0,0,.25)}
.brand-box{position:absolute;left:188px;top:0;width:168px;height:50px;background:var(--white);border:3px solid #3cc0f0;border-top:0;border-radius:0 0 4px 4px;display:flex;align-items:center;justify-content:center;z-index:3}
.brand-name{font-family:"Bree Serif",Georgia,serif;font-weight:400;font-size:18px;line-height:20px;color:var(--ink)}
.app-name{position:absolute;left:371px;top:10px;font-family:"Open Sans",Arial,sans-serif;font-style:italic;font-size:17px;color:var(--white)}
.main-nav{position:absolute;left:563px;top:0;height:43px;display:flex}
.main-nav a{display:block;height:43px;line-height:43px;padding:0 16px;font-family:"Bree Serif",Georgia,serif;font-size:11px;color:var(--white);text-decoration:none;letter-spacing:.3px}
.main-nav a.active{background:#1f1f1f;padding:0 13px}
.stage-lip{position:absolute;left:166px;top:43px;width:820px;height:23px;background:var(--sky-deep);clip-path:polygon(0 0,100% 0,98% 100%,2% 100%)}
.hero-frame{position:absolute;left:166px;top:66px;width:820px;height:239px;background:var(--white)}
.hero{position:absolute;left:16px;top:17px;width:788px;height:205px;background:linear-gradient(180deg,#3b4fa0 0%,#7b6fc4 40%,#c88ac8 70%,#4a5a92 100%);overflow:hidden}
.hero-title{position:absolute;left:29px;top:46px;font-family:"Bree Serif",Georgia,serif;font-size:26px;color:var(--white);text-shadow:1px 1px 2px rgba(0,0,0,.5)}
.hero-text{position:absolute;left:29px;top:86px;width:260px;font-size:10px;line-height:12px;color:var(--white)}
.hero-btn{position:absolute;left:29px;top:125px;width:94px;height:40px;background:#111;border-radius:4px;color:var(--white);font-family:"Bree Serif",Georgia,serif;font-size:10px;display:flex;align-items:center;padding-left:13px;gap:10px}
.hero-tab{position:absolute;left:458px;top:268px;width:236px;height:20px;background:var(--white);border-radius:14px 14px 0 0;display:flex;justify-content:center;align-items:center;gap:10px}
.hero-tab i{width:13px;height:13px;border-radius:50%;background:#888;box-shadow:inset 0 1px 2px rgba(0,0,0,.4)}
.hero-tab i.on{background:#eee;box-shadow:inset 0 1px 2px rgba(0,0,0,.25)}
.content{position:absolute;left:166px;top:310px;width:820px;height:684px;background:var(--white);box-shadow:0 8px 14px rgba(0,0,0,.25)}
.block{position:absolute}
.block h2{font-family:"Bree Serif",Georgia,serif;font-weight:400;font-size:20px;color:var(--head);height:26px;line-height:26px;margin-bottom:4px}
.block h2 span{color:var(--sky)}
table{border-collapse:collapse;width:100%;font-size:11.5px}
th{background:var(--ink);color:var(--white);font-weight:400;text-align:left;height:27px;padding:0 6px;border-right:1px solid #777}
th:last-child{border-right:0}
td{height:26.5px;padding:0 6px;border-bottom:1px solid var(--rule);color:var(--text)}
td a{color:var(--link);text-decoration:underline}
td.num{text-align:center}
.flag{display:inline-block;width:10px;height:10px;border-radius:50%;vertical-align:-1px;margin-left:4px}
.flag.red{background:#e02020}
.flag.amber{background:#f3c813}
.pager{position:absolute;left:0;width:100%;height:32px;border-top:1px solid var(--rule);border-bottom:1px solid var(--rule);display:flex;justify-content:center;align-items:center;gap:2px}
.pager b,.pager span{display:flex;align-items:center;justify-content:center;height:22px;font-size:11px;border-radius:3px}
.pager b{width:23px;background:linear-gradient(180deg,#6a7b98,var(--pager-dark));color:var(--white);font-weight:400}
.pager span{width:18px;background:#e9e9e9;border:1px solid #c4c4c4;color:#555}
.new-request{position:absolute;left:421px;top:413px;width:383px;height:45px;border-radius:5px;background:linear-gradient(180deg,var(--green-top),var(--green-bot));border:1px solid #69ad2a;font-family:"Bree Serif",Georgia,serif;font-size:15px;color:#2f4d10;display:flex;align-items:center;justify-content:center}
.foot-nav{position:absolute;left:166px;top:994px;width:820px;height:57px;background:var(--ink);display:flex;justify-content:center;align-items:center}
.foot-nav a{font-family:"Bree Serif",Georgia,serif;font-size:11px;color:var(--white);text-decoration:none;padding:0 17px}
.foot-lip{position:absolute;left:166px;top:1051px;width:820px;height:24px;background:linear-gradient(180deg,#bbb,#d6d6d6);clip-path:polygon(2% 0,98% 0,100% 100%,0 100%)}
.foot-box{position:absolute;left:166px;top:1075px;width:820px;height:89px;background:var(--white);box-shadow:0 6px 10px rgba(0,0,0,.2)}
.foot-brand{position:absolute;left:22px;top:34px}
.copyright{position:absolute;right:25px;top:40px;font-family:Arial,Helvetica,sans-serif;font-size:10.5px;color:#444}
</style>
</head>
<body>
<div class="sky-band"></div>
<header class="topbar"></header>
<div class="brand-box"><span class="brand-name">Norvane Group</span></div>
<div class="app-name">Tessaro Desk</div>
<nav class="main-nav">
  <a class="active" href="#">HOME</a><a href="#">PERMITS</a><a href="#">REPORT</a><a href="#">SEARCH</a><a href="#">ADMIN</a><a href="#">HELP</a>
</nav>
<div class="stage-lip"></div>
<div class="hero-frame">
  <div class="hero" role="img" aria-label="Petrochemical refinery plant lit at dusk under a purple sky">
    <div class="hero-title">Norvane Industries</div>
    <div class="hero-text">sit amet, consectetur adipiscing elit. In interdum aliquet orci, vitae ornare erat elementum et.</div>
    <div class="hero-btn">Read More
      <svg width="10" height="14" viewBox="0 0 10 14"><path d="M2 1l6 6-6 6" fill="none" stroke="#fff" stroke-width="3"/></svg>
    </div>
  </div>
</div>
<div class="hero-tab" style="left:624px"><i class="on"></i><i></i><i></i><i></i></div>

<main class="content">
  <section class="block" style="left:16px;top:30px;width:382px;height:170px">
    <h2><span>New</span> Requests</h2>
    <table>
      <tr><th style="width:91px">Request No.</th><th style="width:127px">Requested Date</th><th>Branch</th></tr>
      <tr><td><a href="#">56-0003</a></td><td>20/4/2013</td><td>GC1</td></tr>
      <tr><td><a href="#">56-0004</a></td><td>20/4/2013</td><td>GC2</td></tr>
    </table>
    <div class="pager" style="top:162px"><b>‹</b><span>1</span><span>2</span><span>3</span><span>4</span><b>›</b></div>
  </section>

  <section class="block" style="left:421px;top:30px;width:383px;height:170px">
    <h2><span>My Working</span> Requests</h2>
    <table>
      <tr><th style="width:92px">Request No.</th><th style="width:101px">Requested Date</th><th>Status</th></tr>
      <tr><td><a href="#">55-0200</a></td><td>20/4/2013</td><td>Waiting for process</td></tr>
      <tr><td><a href="#">55-0210</a></td><td>20/4/2013</td><td>In progress</td></tr>
      <tr><td><a href="#">55-0300</a></td><td>20/4/2013</td><td>Incomplete document</td></tr>
      <tr><td><a href="#">55-0301</a></td><td>20/4/2013</td><td>Cancel requested</td></tr>
    </table>
    <div class="pager" style="top:162px;border-top:0"><b>‹</b><span>1</span><span>2</span><span>3</span><span>4</span><b>›</b></div>
  </section>

  <section class="block" style="left:12px;top:240px;width:791px">
    <h2><span>Expiring</span> Permits</h2>
    <table>
      <tr><th style="width:101px">Permit No</th><th style="width:103px">Expire Date</th><th style="width:214px">Permit Name</th><th style="width:103px">Branch</th><th style="width:133px">Required Time (Day)</th><th>Required Time (Day)</th></tr>
      <tr><td><a href="#">AB56001</a></td><td>25/3/2013</td><td>Permit Name ###10</td><td>GC1</td><td class="num">30 <span class="flag red"></span></td><td class="num">-40</td></tr>
      <tr><td><a href="#">BIO5502</a></td><td>24/3/2013</td><td>Permit Name ###20</td><td>GC2</td><td class="num">60 <span class="flag amber"></span></td><td class="num">15</td></tr>
    </table>
    <div class="pager" style="top:117px;border-top:0"><b>‹</b><span>1</span><span>2</span><span>3</span><span>4</span><b>›</b></div>
  </section>

  <section class="block" style="left:16px;top:408px;width:382px">
    <h2><span>My In Progress</span> Requests</h2>
    <table>
      <tr><th style="width:92px">Request No.</th><th style="width:126px">Requested Date</th><th>Status</th></tr>
      <tr><td><a href="#">56-0003</a></td><td>20/4/2013</td><td>ระหว่างดำเนินการ</td></tr>
      <tr><td><a href="#">56-0004</a></td><td>20/4/2013</td><td>รอดำเนินการ</td></tr>
    </table>
    <div class="pager" style="top:198px"><b>‹</b><span>1</span><span>2</span><span>3</span><span>4</span><b>›</b></div>
  </section>

  <div class="new-request">New Request</div>

  <section class="block" style="left:421px;top:464px;width:383px">
    <h2><span>Recent Completed</span> Requests</h2>
    <table>
      <tr><th style="width:118px">Request No.</th><th>Completed Date</th></tr>
      <tr><td><a href="#">55-0100</a></td><td>20/4/2013</td></tr>
      <tr><td><a href="#">55-0088</a></td><td>20/4/2013</td></tr>
      <tr><td><a href="#">55-0002</a></td><td>20/4/2013</td></tr>
    </table>
    <div class="pager" style="top:142px;border-top:0"><b>‹</b><span>1</span><span>2</span><span>3</span><span>4</span><b>›</b></div>
  </section>
</main>

<nav class="foot-nav">
  <a href="#">HOME</a><a href="#">PERMITS</a><a href="#">REPORT</a><a href="#">SEARCH</a><a href="#">ADMIN</a><a href="#">HELP</a>
</nav>
<div class="foot-lip"></div>
<footer class="foot-box">
  <div class="foot-brand"><span class="brand-name">Norvane Group</span></div>
  <div class="copyright">© Copyright NorvaneGroup.com. All Rights Reserved</div>
</footer>
</body>
</html>
```